elegant beautiful Hang tag for a novelty makeup towel

It's a black hand towel in the shape of a little black dress. it is called VELVET EVENING CLOTH, it is a CLEAN SLATE FACE CLOTH. (doesn't show our makeup stains) Made in USA

Target Market(s)

ALL Women , Makeup artists, novelty THIS WILL BE IN THE HALVERDALE STORES AND PRESCOTWICK STORES.

Industry/Entity Type

Makeup

Contact Information for Business Card

I actually need a hang tag for a homemade handmade towel. I have a logo that I want on the tag and know what we want to say on it, on back needs to say "The essential to every girl's wardrobe. So when the little black dress comes off, our VELVET EVENING CLOTH is there to help you wash your day away. Include website www.velveteveningcloth.example OH INCLUDE TM (trademark sign next to logo please. Also, in small print on back from the makers of THE ORIGINAL CLEAN SLATE FACE CLOTH. handmade in USA. also CLEAN SLATE FACE CLOTH IN big font on front under logo sign with light colored pink lips after 'NO SHOW" but have no idea about fonts, graphics, placement or design. Want it classy, elegant, girly! COLORS LIGHT BEIGER BACKGROUND WITH BLACK WRITING/ DESIGNS

Font styles to use
Serif
Decorative
Script

Colors
fff3d1

Requirements
Must have
• Black cream girly , also state in big writing that it's a " clean slate face cloth" with a tiny light pink lip between the show and makeup. Include www.velveteveningcloth.example Quillfern Goods, LLC
Nice to have
• Perhaps an outline of a little black dress. A black scroll edge of some sort around card. Classy

```html
<!DOCTYPE html>
<html lang="en">
<head>
<meta charset="utf-8">
<title>Velvet Evening Cloth – Hang Tag</title>
<link rel="stylesheet" href="https://fonts.googleapis.com/css2?family=Gochi+Hand&family=Raleway:ital,wght@0,300;1,300&display=swap">
<style>
  :root {
    --page: #ffffff;
    --tag-black: #000000;
    --cream: #fff3d1;
    --stitch: #4a2410;
    --ink: #111111;
    --rule: #333333;
  }
  html, body {
    margin: 0;
    padding: 0;
    width: 1200px;
    height: 709px;
    overflow: hidden;
    background: var(--page);
  }
  .hang-tag {
    display: block;
    width: 1200px;
    height: 709px;
  }
  .tag-body { fill: var(--tag-black); }
  .label-plate { fill: var(--cream); }
  .label-stitch {
    fill: none;
    stroke: var(--stitch);
    stroke-width: 3;
    stroke-dasharray: 14 8;
    stroke-linecap: butt;
  }
  .brand-name {
    font-family: "Gochi Hand", cursive;
    font-size: 56px;
    fill: var(--ink);
    letter-spacing: 6px;
  }
  .tagline {
    font-family: "Raleway", sans-serif;
    font-weight: 300;
    font-size: 23px;
    fill: var(--ink);
    letter-spacing: 0.5px;
  }
  .tagline-accent { font-style: italic; }
  .tagline-rule {
    stroke: var(--rule);
    stroke-width: 1.2;
  }
</style>
</head>
<body>
<svg class="hang-tag" viewBox="0 0 1148 680" preserveAspectRatio="none" xmlns="http://www.w3.org/2000/svg">
  <defs>
    <path id="bracket-label" d="
      M578,38
      Q540,75 320,92
      Q170,102 150,130
      Q108,170 100,215
      Q96,292 68,325
      Q96,358 100,435
      Q108,480 150,520
      Q170,550 320,560
      Q540,575 578,620
      Q616,575 836,560
      Q986,550 1006,520
      Q1048,480 1056,435
      Q1060,358 1088,325
      Q1060,292 1056,215
      Q1048,170 1006,130
      Q986,102 836,92
      Q616,75 578,38 Z"/>
  </defs>

  <rect class="tag-body" x="50" y="33" width="1052" height="600" rx="34" ry="34"/>

  <use class="label-plate" href="#bracket-label"/>
  <use class="label-stitch" href="#bracket-label" transform="translate(578 329) scale(0.955 0.935) translate(-578 -329)"/>

  <text class="brand-name" x="576" y="324" text-anchor="middle" textLength="900" lengthAdjust="spacing">VELVET EVENING CLOTH</text>

  <line class="tagline-rule" x1="122" y1="367" x2="335" y2="367"/>
  <text class="tagline" x="578" y="376" text-anchor="middle">CLEAN SLATE <tspan class="tagline-accent">FACE</tspan> CLOTH</text>
  <line class="tagline-rule" x1="820" y1="367" x2="1015" y2="367"/>
</svg>
</body>
</html>
```